Tolvane Air and Electrical Website

Simple and easy to use website for a Electrical and Air Conditioning contracting business.Use stock photosOnline contact portallogo still to be supplied

Target Market(s)

Mums and Dads who want a local contractor

Coding

Coded - Design and coding required

Number of Pages Required

2 page

Font styles to use
Sans Serif

Colors
f04a50
3276b5
33a6d7

Requirements
Must have
• Simple and easy to use
• Ph number
• 4 web address; linked to page
• 0417385926
• tolvane.com.au
• tolvaneelectrical.com.au
• tolvaneairandelectrical.com.au
• tolvaneair.com.au
Nice to have
• Split System Air Con Picture
• Electrical Pictures

```html
<!DOCTYPE html>
<html lang="en">
<head>
<meta charset="utf-8">
<title>Tolvane Air and Electrical</title>
<link rel="stylesheet" href="https://fonts.googleapis.com/css2?family=Open+Sans:wght@400;700;800&family=Baloo+2:wght@600;700&family=Montserrat:wght@500;600&family=Arimo:ital,wght@0,400;0,700;1,400&display=swap">
<style>
:root{
  --red:#ec2027;
  --blue:#1273bf;
  --brand-blue:#3276b5;
  --sky:#4a8ccb;
  --accent:#4f8ff0;
  --label:#3b8fd7;
  --dark:rgba(28,38,54,.88);
  --band:#ececec;
  --grey-bg:#efefef;
  --text:#222;
  --muted:#9a9a9a;
  --white:#fff;
}
*{margin:0;padding:0;box-sizing:border-box}
html,body{width:1025px;height:1200px;overflow:hidden;background:var(--white);font-family:"Arimo",Arial,sans-serif;color:var(--text)}
.page{position:relative;width:1025px;height:1200px}
.abs{position:absolute}

.logo{left:109px;top:20px;display:flex;align-items:center;gap:7px}
.logo-mark{width:22px;height:22px;background:var(--red)}
.logo-name{font-family:"Open Sans",sans-serif;font-weight:800;font-size:20px;color:var(--blue);letter-spacing:.5px}

.contact-item{top:23px;display:flex;gap:8px}
.contact-icon{width:24px;height:24px;border-radius:4px;background:var(--red);display:flex;align-items:center;justify-content:center}
.contact-label{font-family:"Open Sans",sans-serif;font-weight:800;font-size:14px;color:var(--blue);line-height:14px}
.contact-value{font-size:11px;color:var(--red);margin-top:3px}

.hero{left:0;top:85px;width:1025px;height:398px;background:linear-gradient(100deg,#5b9ad2 0%,#3f80c2 45%,#4a8dcc 100%)}
.nav{left:107px;top:65px;width:813px;height:42px;background:var(--blue);font-family:"Open Sans",sans-serif;font-weight:800;font-size:12px;color:var(--white)}
.nav a{position:absolute;top:13px;color:var(--white);text-decoration:none;transform:translateX(-50%);white-space:nowrap}
.nav .sep{position:absolute;top:13px;width:1px;height:14px;background:rgba(255,255,255,.35)}
.nav .active-bar{position:absolute;left:13px;top:39px;width:74px;height:3px;background:var(--red)}

.hero-card{left:566px;top:203px;width:255px;height:184px;background:var(--dark);padding:24px 16px}
.hero-label{font-family:"Open Sans",sans-serif;font-weight:700;font-size:11.5px;color:var(--label);padding-bottom:2px;border-bottom:1px solid rgba(255,255,255,.25);width:216px}
.hero-title{margin-top:10px;font-family:"Baloo 2",sans-serif;font-weight:700;font-size:15.5px;line-height:20px;color:var(--white)}
.btn-learn{display:inline-block;margin-top:13px;width:74px;height:25px;border-radius:3px;background:#2f77c1;color:var(--white);font-family:"Open Sans",sans-serif;font-weight:800;font-size:7.5px;text-align:center;line-height:25px}

.band{left:0;top:483px;width:1025px;height:40px;background:var(--band)}
.band-text{left:193px;top:497px;font-family:"Open Sans",sans-serif;font-weight:700;font-size:10px;color:var(--accent)}
.btn-quote{left:600px;top:490px;width:98px;height:26px;background:var(--accent);color:var(--white);font-family:"Open Sans",sans-serif;font-weight:700;font-size:8px;text-align:center;line-height:26px}
.btn-projects{left:700px;top:490px;width:113px;height:26px;border:1px solid #cfcfcf;color:#888;font-family:"Open Sans",sans-serif;font-weight:700;font-size:8px;text-align:center;line-height:24px}

.feature{top:592px;width:220px;text-align:center;transform:translateX(-50%)}
.feature svg{height:40px}
.feature h2{font-family:"Baloo 2",sans-serif;font-weight:700;font-size:19px;color:#2a2a2a;margin-top:20px;letter-spacing:.5px}
.feature p{margin-top:8px;font-size:9px;line-height:18px;color:var(--muted)}

.testimonials-bg{left:0;top:816px;width:1025px;height:352px;background:var(--grey-bg)}
.testimonials-panel{left:183px;top:856px;width:695px;height:275px;background:#ececec}
.testimonials-title{left:207px;top:873px;font-family:"Montserrat",sans-serif;font-weight:600;font-size:17px;color:#333}
.arrow-btn{top:875px;width:24px;height:24px;border:1px solid #c9c9c9;display:flex;align-items:center;justify-content:center}
.rule{left:207px;top:908px;width:609px;height:1px;background:#d8d8d8}
.rule-accent{left:207px;top:907px;width:16px;height:2px;background:var(--accent)}

.quote-card{top:925px;width:297px;height:135px;background:var(--white)}
.quote-mark{left:0;top:0;width:24px;height:24px;background:#bdbdbd;color:var(--white);font-family:Georgia,serif;font-style:italic;font-size:20px;text-align:center;line-height:30px}
.quote-text{position:absolute;font-style:italic;font-size:9px;line-height:18px;color:#222}
.quote-tail{position:absolute;left:16px;bottom:-8px;width:0;height:0;border-top:8px solid var(--white);border-right:10px solid transparent}
.author{top:1075px;font-size:9px;font-weight:700;color:#222}
.stars{top:1088px;font-size:8px;color:var(--accent);letter-spacing:-1px}

.footer{left:0;top:1168px;width:1025px;height:32px;background:var(--brand-blue)}
</style>
</head>
<body>
<div class="page">

  <div class="abs logo">
    <span class="logo-mark"></span>
    <span class="logo-name">TOLVANE</span>
  </div>

  <div class="abs contact-item" style="left:676px">
    <span class="contact-icon">
      <svg width="14" height="14" viewBox="0 0 24 24"><path fill="#fff" d="M6.6 10.8a15.1 15.1 0 0 0 6.6 6.6l2.2-2.2c.3-.3.7-.4 1-.2 1.1.4 2.3.6 3.6.6.6 0 1 .4 1 1V20c0 .6-.4 1-1 1A17 17 0 0 1 3 4c0-.6.4-1 1-1h3.5c.6 0 1 .4 1 1 0 1.3.2 2.5.6 3.6.1.3 0 .7-.2 1l-2.3 2.2z"/></svg>
    </span>
    <div><div class="contact-label">CALL US:</div><div class="contact-value">040 000 000</div></div>
  </div>

  <div class="abs contact-item" style="left:796px">
    <span class="contact-icon">
      <svg width="14" height="12" viewBox="0 0 24 18"><rect x="1" y="1" width="22" height="16" fill="none" stroke="#fff" stroke-width="2"/><path d="M1 1l11 9 11-9M1 17l8-7M23 17l-8-7" fill="none" stroke="#fff" stroke-width="2"/></svg>
    </span>
    <div><div class="contact-label">EMAIL US:</div><div class="contact-value">tolvane@mail.com</div></div>
  </div>

  <div class="abs hero" role="img" aria-label="Photo of a smiling electrician in a blue hard hat in front of an electrical switchboard, blue tinted"></div>

  <nav class="abs nav">
    <a href="#" style="left:51px">HOME</a>
    <span class="sep" style="left:94px"></span>
    <a href="#" style="left:138px">ABOUT US</a>
    <span class="sep" style="left:190px"></span>
    <a href="#" style="left:247px">OUR SERVICES</a>
    <span class="sep" style="left:309px"></span>
    <a href="#" style="left:353px">CONTACT</a>
    <span class="active-bar"></span>
  </nav>

  <div class="abs hero-card">
    <div class="hero-label">TOLVANE AIR AND ELECTRICAL</div>
    <div class="hero-title">All of our electricians are<br>A-Grade qualified and are<br>Skilful, Professional,<br>and Courteous.</div>
    <span class="btn-learn">LEARN MORE</span>
  </div>

  <div class="abs band"></div>
  <div class="abs band-text">WE GUARANTEE CLIENT FOCUSSED ATTENTION TO DETAIL THAT YOU CAN TRUST</div>
  <div class="abs btn-quote">REQUEST A QUOTE</div>
  <div class="abs btn-projects">CHECK OUR PROJECTS</div>

  <div class="abs feature" style="left:236px">
    <svg viewBox="0 0 66 40" width="66"><g fill="#ec2027"><circle cx="10" cy="15" r="6.5"/><circle cx="33" cy="9" r="8"/><circle cx="56" cy="15" r="6.5"/><rect x="1" y="23" width="18" height="17" rx="3"/><rect x="21" y="19" width="24" height="21" rx="3"/><rect x="47" y="23" width="18" height="17" rx="3"/></g></svg>
    <h2>About Us</h2>
    <p>With over 17 years' experience in the Electrical Industry, Tolvane Electrical provides a superior level of knowledge, a broad range of products and a high standard of customer service.</p>
  </div>

  <div class="abs feature" style="left:512px">
    <svg viewBox="0 0 40 40" width="40"><path d="M3 37V20A17 17 0 1 1 20 37z" fill="none" stroke="#ec2027" stroke-width="3"/><path d="M15 15a5 5 0 1 1 7 4.5c-1.5.7-2 1.5-2 3v1.5" fill="none" stroke="#ec2027" stroke-width="3"/><circle cx="20" cy="29" r="2" fill="#ec2027"/></svg>
    <h2>Why Us</h2>
    <p>On Time We arrive on time. If there is an unavoidable delay we'll call ahead to let you know when we'll be there .We also respond to your phone calls and emails within 24 hours</p>
  </div>

  <div class="abs feature" style="left:793px;top:592px">
    <svg viewBox="0 0 40 40" width="40"><g fill="#ec2027"><circle cx="20" cy="20" r="15"/><g><rect x="16" y="0" width="8" height="8"/><rect x="16" y="32" width="8" height="8"/><rect x="0" y="16" width="8" height="8"/><rect x="32" y="16" width="8" height="8"/><rect x="16" y="0" width="8" height="8" transform="rotate(45 20 20)"/><rect x="16" y="32" width="8" height="8" transform="rotate(45 20 20)"/><rect x="0" y="16" width="8" height="8" transform="rotate(45 20 20)"/><rect x="32" y="16" width="8" height="8" transform="rotate(45 20 20)"/></g></g><circle cx="20" cy="20" r="9" fill="#fff"/><path d="M13 27l8-8" stroke="#ec2027" stroke-width="4" stroke-linecap="round"/><circle cx="23" cy="17" r="4" fill="#ec2027"/></svg>
    <h2>Services</h2>
    <p style="margin-top:-2px">Whether you are looking for security, data or audio visual systemswe have the tools and skills required If you're looking to expandor further integratedata and technology your electricians areequipped to handle the job.</p>
  </div>

  <div class="abs testimonials-bg"></div>
  <div class="abs testimonials-panel"></div>
  <div class="abs testimonials-title">Testimonials</div>
  <div class="abs arrow-btn" style="left:763px"><svg width="8" height="12" viewBox="0 0 8 12"><path d="M6 1L1 6l5 5" fill="none" stroke="#777" stroke-width="1.5"/></svg></div>
  <div class="abs arrow-btn" style="left:792px"><svg width="8" height="12" viewBox="0 0 8 12"><path d="M2 1l5 5-5 5" fill="none" stroke="#777" stroke-width="1.5"/></svg></div>
  <div class="abs rule"></div>
  <div class="abs rule-accent"></div>

  <div class="abs quote-card" style="left:207px">
    <div class="abs quote-mark">&ldquo;</div>
    <p class="quote-text" style="left:39px;top:22px;width:250px">Excellent service. Declan came and quoted at the agreed time. The team showed up on time an completed on time. Declan and his guys were friendly and professional and I would highly recommend them. I will look to them for any future work.</p>
    <span class="quote-tail"></span>
  </div>
  <div class="abs quote-card" style="left:520px">
    <div class="abs quote-mark">&ldquo;</div>
    <p class="quote-text" style="left:44px;top:34px;width:235px">Declan was a pleasure to work with. He and his team completed our job expertly, efficiently and cost-effectively. Many thanks!</p>
    <span class="quote-tail"></span>
  </div>

  <div class="abs author" style="left:207px">Maren from Preston, VIC</div>
  <div class="abs stars" style="left:207px">★★★★★</div>
  <div class="abs author" style="left:519px">Colin R from Northcote, VIC</div>
  <div class="abs stars" style="left:519px">★★★★★</div>

  <div class="abs footer"></div>
</div>
</body>
</html>
```